2 Business Card Designs

Need two business cards designed:
1) for lumora studio (wedding video) website is lumorastudio.com.au
2) for lumora studio (corporate video) website is lumorastudio.net.au

I am looking for something simple, no fancy shapes etc. Just elegant, simple and classy.

Both companies are video companies, one specialising in weddings the other corporate videos. Neither card needs to have any pics of video or camera related images. Please use same colour schemes as respective websites.

Logo is the same but can change colour.

Industry/Entity Type

Camera

Requirements
Must have
• Logo should be either all white or a colour to match websites
Should not have
• swirls, flowers, shapes, etc.

```html
<!DOCTYPE html>
<html lang="en">
<head>
<meta charset="utf-8">
<title>Lumora Studio – Business Card</title>
<link rel="stylesheet" href="https://fonts.googleapis.com/css2?family=Comfortaa:wght@400&family=Pathway+Gothic+One&display=swap">
<style>
  :root {
    --page-bg: #ffffff;
    --card-bg: #ffffff;
    --card-edge: #c9c9c9;
    --card-shadow: rgba(0, 0, 0, 0.22);
    --logo-grey: #555555;
    --lens-blue: #5aa9e6;
    --band-tint: #d9d9bf;
    --url-ink: #333333;
    --detail-ink: #5a5a5a;
    --strip-grey: #b8b2b2;
  }
  html, body {
    margin: 0;
    padding: 0;
    width: 945px;
    height: 1200px;
    overflow: hidden;
    background: var(--page-bg);
  }
  .sheet {
    position: relative;
    width: 945px;
    height: 1200px;
  }
  .card {
    position: absolute;
    left: 46px;
    width: 852px;
    height: 540px;
    background: var(--card-bg);
    border: 2px solid var(--card-edge);
    border-radius: 38px;
    box-shadow: 0 4px 10px var(--card-shadow);
    overflow: hidden;
    box-sizing: border-box;
  }
  .card--front { top: 38px; }
  .card--back { top: 623px; }

  .brand {
    position: absolute;
    left: 0;
    right: 0;
    top: 160px;
    display: flex;
    align-items: center;
    justify-content: center;
    gap: 26px;
  }
  .brand__dot {
    width: 46px;
    height: 46px;
    border-radius: 50%;
    background: var(--lens-blue);
  }
  .brand__name {
    margin: 0;
    font-family: "Comfortaa", sans-serif;
    font-weight: 400;
    font-size: 92px;
    line-height: 1;
    color: var(--logo-grey);
    letter-spacing: 1px;
  }
  .web-band {
    position: absolute;
    left: 19px;
    top: 406px;
    width: 640px;
    height: 48px;
    background: linear-gradient(to right, var(--band-tint) 0%, #eeeee2 45%, rgba(255,255,255,0) 100%);
  }
  .web-band__url {
    position: absolute;
    left: 184px;
    top: 50%;
    transform: translateY(-50%);
    margin: 0;
    font-family: "Comfortaa", sans-serif;
    font-size: 27px;
    color: var(--url-ink);
    white-space: nowrap;
  }

  .film-strip {
    position: absolute;
    left: 390px;
    top: 30px;
    width: 420px;
    height: 420px;
  }
  .contact {
    position: absolute;
    left: 112px;
    top: 118px;
    margin: 0;
    padding: 0;
    list-style: none;
    font-family: "Pathway Gothic One", sans-serif;
    font-size: 44px;
    line-height: 57px;
    color: var(--detail-ink);
  }
</style>
</head>
<body>
<main class="sheet">
  <section class="card card--front" aria-label="Card front">
    <div class="brand">
      <span class="brand__dot" aria-hidden="true"></span>
      <h1 class="brand__name">lumora studio</h1>
    </div>
    <div class="web-band">
      <p class="web-band__url">www.lumorastudio.com.au</p>
    </div>
  </section>

  <section class="card card--back" aria-label="Card back">
    <svg class="film-strip" viewBox="0 0 420 420" role="img" aria-label="Tilted film strip graphic in soft grey fading downward">
      <defs>
        <linearGradient id="stripFade" x1="0" y1="0" x2="0" y2="1">
          <stop offset="0" stop-color="#b8b2b2"/>
          <stop offset="0.82" stop-color="#b8b2b2"/>
          <stop offset="1" stop-color="#b8b2b2" stop-opacity="0.15"/>
        </linearGradient>
      </defs>
      <rect x="40" y="24" width="330" height="370" fill="url(#stripFade)" transform="rotate(-9 205 209)"/>
    </svg>
    <ul class="contact">
      <li>Comapany name</li>
      <li>Address</li>
      <li>Sample name</li>
      <li>Phone#</li>
      <li>Website</li>
    </ul>
  </section>
</main>
</body>
</html>
```